Quorvella Website Redesign

We need a redesign of the company website.

We're a company, based in the UK, called Quorvella. We develop software for the Healthcare Industry, used by medical professionals throughout the UK on a daily basis.

We have a suite of tools that form the Quorvella Platform, and all are web-based.

We want to communicate that our software is not only innovative but is the best available, easy to use, and provides exceptional quality and RoI.

Additionally, we want our existing customers to be able to see what else we can offer them.

A site map is attached.
Updates

Hi Everyone,

As we approach the deadline for submissions, we’ve shortlisted threedesigns that we felt were the best of the submissions and have asked thedesigners to make some additional changes and produce some content pages so wecan see what’s beneath the Home page in the rest of the site.

Thank you all for your submissions – there was an awful lot ofdisagreement among everyone here over which designs we thought were best andsome of those that haven’t made it into the final three were very well liked.

Those in the final three have been messaged individually and have theirdesigns as the only non-eliminated ones showing. We would ask at this stagethat anyone not in the final three please do no further work or submitadditional designs as we are approaching the deadline and will not be able toprovide sufficient feedback to allow any changes in a short space of time.

Kind regards,
The Quorvella Team

Target Market(s)

Nurses and medical professionals in western-speaking countries, most notably in the UK.

Predominantly, we expect it will be senior medical staff that will be viewing (and using) our website - some will be existing customers and some will be new or potential customers.

Industry/Entity Type

Medical

Requirements
Must have
• Area to showcase and provide information about products.
• Company information - who we are and why you should choose us.
• News and events - blog, archive newsletters, publications, etc.
• Support section for existing customers - FAQ, Forum, Manuals.
• Contact page.
• We also feel that we'd like to have our telephone number and primary email address visible at all times, with an immediate ability for users to request a demonstration.
Nice to have
• A "My Quorvella" area would be nice at some point, though that's something for further down the line.

```html
<!DOCTYPE html>
<html lang="en">
<head>
<meta charset="utf-8">
<title>Quorvella Health</title>
<link rel="stylesheet" href="https://fonts.googleapis.com/css2?family=Arimo:wght@400;700&display=swap">
<style>
:root{
  --black:#000;
  --nav:#1c1c1c;
  --blue:#1a8fe6;
  --text:#222;
  --muted:#8a8a8a;
  --page-top:#f7f7f7;
  --page-bottom:#e9e9e9;
  --panel:#fff;
  --tile-1:#cfcfcf;
  --tile-2:#bebebe;
  --tile-3:#b1b1b1;
  --btn:#2aa6dc;
}
*{margin:0;padding:0;box-sizing:border-box}
html,body{width:955px;height:1200px;overflow:hidden}
body{font-family:"Arimo",Arial,sans-serif;color:var(--text);position:relative;
  background:linear-gradient(to bottom,var(--page-top) 0,#fbfbfb 300px,var(--page-bottom) 322px,var(--page-bottom) 1060px,#dcdcdc 1080px,#dcdcdc 100%)}
.abs{position:absolute}
.topbar{left:0;top:0;width:955px;height:22px;background:var(--black)}
.nav{left:0;top:22px;width:955px;height:46px;background:var(--nav)}
.nav a{position:absolute;top:0;line-height:46px;color:#fff;font-size:15px;text-decoration:none}
.nav .home{left:55px;width:97px;text-align:center;background:#fff;color:#222}
.nav .sep{position:absolute;top:14px;width:1px;height:12px;border-left:1px dotted #777}
.rss{left:857px;top:10px;width:18px;height:18px;background:#f39a1d;border-radius:3px}
.logo{left:44px;top:104px;font-size:37px;font-weight:700;color:var(--blue);letter-spacing:-.5px}
.logo-rule{left:45px;top:152px;width:280px;height:2px;background:#bbb}
.tagline{left:45px;top:157px;font-size:16px;font-weight:700;color:#999}
.contact{right:42px;top:86px;text-align:right;font-size:11.5px;line-height:13.5px;color:#333}
.contact b{color:var(--blue)}
.contact .k{color:var(--blue)}
.panel{left:36px;top:210px;width:884px;height:912px;background:var(--panel);box-shadow:0 0 2px rgba(0,0,0,.08)}
.hero{left:53px;top:236px;width:583px;height:250px;background:linear-gradient(120deg,#c9d3d8,#e8eef1 45%,#9fc3d8 60%,#d7dde0)}
.replay{left:63px;top:460px;background:#5bbcd6;color:#fff;font-size:10px;font-weight:700;padding:3px 9px}
.tile{left:636px;width:267px;display:flex;align-items:center}
.tile .ico{width:58px;height:58px;border-radius:9px;margin-left:14px;background:linear-gradient(#bfe6f4,#56b5dc);border:2px solid #e9f5fa}
.tile span{margin-left:10px;color:#fff;font-size:22px;font-weight:700}
h2{position:absolute;font-size:23px;font-weight:400;color:#333}
h2 b{color:var(--blue);font-weight:700}
.ph{background:linear-gradient(135deg,#d6d9dc,#9aa3a9)}
.links{left:80px;top:682px;font-size:11px;font-weight:700;color:var(--blue)}
.links div{display:flex;align-items:center;height:29px}
.links i{display:inline-block;width:20px;height:20px;border:1px solid #aaa;background:#eee;margin-right:7px;border-radius:2px}
.more{font-size:11px;color:#222;display:flex;align-items:center}
.more::before{content:"";width:10px;height:10px;border-radius:50%;background:#666;margin-right:9px}
.copy{font-size:10.5px;line-height:15.6px;color:#222}
.copy p{margin-bottom:8px}
.copy h4{font-size:10.5px;font-weight:700}
.login{font-size:10.5px;color:#222}
.field{position:absolute;width:172px;height:24px;border:1px solid #ccc;border-radius:4px;background:#fff}
.btn{left:801px;top:620px;width:74px;height:26px;border-radius:13px;background:var(--btn);color:#fff;font-size:11px;font-weight:700;text-align:center;line-height:26px}
.blue{color:var(--blue)}
.foot{font-size:11px;color:#222}
</style>
</head>
<body>
<div class="abs topbar"></div>
<nav class="abs nav">
  <a class="home">HOME</a>
  <a style="left:195px">ABOUT QUORVELLA</a><span class="sep" style="left:338px"></span>
  <a style="left:360px">NEWS &amp; EVENTS</a><span class="sep" style="left:504px"></span>
  <a style="left:539px">SUPPORTS</a><span class="sep" style="left:651px"></span>
  <a style="left:690px">CONTACT US</a>
  <span class="abs rss"></span>
</nav>

<div class="abs logo">QuorvellaHealth</div>
<div class="abs logo-rule"></div>
<div class="abs tagline">Bringing Technology to Healthcare</div>

<div class="abs contact">
  <b>Quorvella</b><br>48 Alder Crescent Road,<br>London N7 2QJ, United Kingdom<br>
  <span class="k">T:</span> +44 (0) 208 555 0142 <span class="k">F:</span> +44 (0) 208 555 0187<br><br>
  Republic Of Ireland &nbsp;<span class="k">T:</span> +353 (0) 861 555 204<br><br>
  Greece and Cyprus <span class="k">T:</span> +357 995 55318
</div>

<div class="abs panel"></div>
<div class="abs hero" role="img" aria-label="Smiling nurse in blue scrubs seated in a hospital ward with monitors and infusion pumps"></div>
<div class="abs replay">REPLAY</div>
<div class="abs tile" style="top:236px;height:87px;background:var(--tile-1)"><i class="ico"></i><span>My Quorvella</span></div>
<div class="abs tile" style="top:323px;height:82px;background:var(--tile-2)"><i class="ico"></i><span>Request a Demo</span></div>
<div class="abs tile" style="top:405px;height:81px;background:var(--tile-3)"><i class="ico"></i><span>News, blog feed</span></div>

<h2 style="left:84px;top:519px">Welcome To <b>Quorvella</b></h2>
<div class="abs ph" style="left:80px;top:573px;width:178px;height:99px" role="img" aria-label="Two laboratory scientists in white coats at a workstation"></div>
<div class="abs links">
  <div><i></i>Ut lortiscidunt vullan vendiame</div>
  <div><i></i>Ut lortiscidunt vullan vendiame</div>
  <div><i></i>Ut lortiscidunt vullan vendiame</div>
</div>
<div class="abs more" style="left:80px;top:769px">Read more</div>

<div class="abs copy" style="left:271px;top:574px;width:310px">
  <p>In today's changing environment, healthcare organisations globally are faced with conflicting challenges; to reduce costs while offering improved healthcare services to patients.</p>
  <p>QUORVELLA solutions exploit opportunities offered by the latest technological advances. Our goal is to help:</p>
  <p>• Reduce clinical errors</p>
  <p>• Improve patient care</p>
  <p>• Improve efficiency</p>
  <p>With our integrated solutions, robust and secure infrastructure and by leveraging our experience, skills and partnerships, Quorvella aims to become one of the leading international service and solution providers to the healthcare industry.</p>
</div>

<h2 style="left:84px;top:833px"><b>Quorvella</b> Solutions</h2>
<div class="abs ph" style="left:78px;top:872px;width:181px;height:101px" role="img" aria-label="Doctor in a white coat working at a computer"></div>
<div class="abs more" style="left:74px;top:1086px">Read more</div>
<div class="abs copy" style="left:271px;top:869px;width:312px">
  <p>Quorvella works in partnership with hospitals and healthcare professionals. Our unique approach, our partnerships with clinical specialists and our technology platform enables us to deliver highly robust and fit-for-purpose solutions.</p>
  <h4>Our Platform</h4>
  <p>Our technology platform, the Clinical Applications Portal, is a robust service based framework that supports our accelerated application development approach. It enables interoperability and integration between Quorvella software modules and other hospital/healthcare systems.</p>
  <h4>Our Products and Services Include</h4>
  <div>• Clinical Systems</div><div style="margin-top:2px">• Clinical Audit Tools</div><div style="margin-top:2px">• Technology Services</div>
</div>

<h2 style="left:637px;top:519px">Customer <b>Login</b></h2>
<div class="abs login" style="left:636px;top:566px">Username:</div>
<div class="field" style="left:703px;top:557px"></div>
<div class="abs login" style="left:636px;top:590px">Password:</div>
<div class="field" style="left:703px;top:589px"></div>
<div class="abs login blue" style="left:637px;top:629px;display:flex;align-items:center"><i style="width:10px;height:10px;border:1px solid #777;margin-right:8px;display:inline-block"></i>Remember Me</div>
<div class="abs btn">Log In</div>
<div class="abs login" style="left:636px;top:650px">Forgot your password?</div>
<div class="abs login" style="left:636px;top:674px">No Account Yet? &nbsp;<span class="blue">Create an Account now</span></div>

<h2 style="left:634px;top:732px">Testimonials</h2>
<div class="abs copy" style="left:636px;top:767px;width:245px">
  <p>Bore vel ut la feugiat augait lortini amcore ver sequate issecte dolestrud tat landipit dolestrud tat adionsendip enim eugait delesse magna adiat. Ed del et, sequam enim alit prat wis nulputem dio et lobor sed do del duipit nis niscill uptat.</p>
  <p>Ustrud magna feuguer iustionullan utatem illam dolore ting ea feugue facidunt non hendreet, quis nulputpatie modolor augiamc onsequisi ero dunt et dolore magna facinismodio exero do consequam eumsan et dolobortie modolummodit verat praessi eliquatis et, con ut la autpat il eugait in verit, Ustrud magna feuguer iustionullan utatem illam dolore ting ea feugue facidunt non hendreet, quis nulputpatie modolor augiamc onsequisi ero dunt et dolore magna facinismodio exero do consequam</p>
  <p class="blue">quissit, susci tie commoluptat. Elit do dolobor</p>
</div>
<div class="abs more" style="left:636px;top:1060px">View All</div>

<div class="abs foot" style="left:44px;top:1138px">Copyright © 2008 Quorvella Ltd</div>
<div class="abs foot" style="right:39px;top:1138px">Terms of Use</div>
<div class="abs foot" style="left:841px;top:1162px;color:#555;display:flex;align-items:center">Chirper<i style="display:inline-block;width:20px;height:20px;background:#c9cdd1;margin-left:8px"></i></div>
</body>
</html>
```